Velmarq's new PowerPoint template

We're Velmarq, an industrial SaaS company based in Rotterdam, Netherlands. We're in need of a new PowerPoint template that can truly represents our corporate brand. Attached is our brand guide and our logo.
Below are some requirements:
- PowerPoint template uses corporate identity and colors.
- PowerPoint template uses PowerPoint theme (for font and color consistency).
- Presentations created with the template shall be crisp and fast
- Presentations created with the template shall not require large disk space
- PowerPoint templates has minimal following template (master) slides:
- Title/Welcome slide
- Agenda slide
- Corporate Vision slide
- Corporate History slide
- Text slide
- Text + Picture slide
- Text + Picture Collage slide
- Picture slide
- Picture + Title slide
- Product Portfolio slide
- Pricing Options slide
- Timeline slide
- Q&A slide
- Closing slide
- Contact slide
- PowerPoint template layout shall be 16:9

```html
<!DOCTYPE html>
<html lang="en">
<head>
<meta charset="utf-8">
<title>Velmarq Presentation Template</title>
<link href="https://fonts.googleapis.com/css2?family=Lato:wght@300;400;700;900&display=swap" rel="stylesheet">
<style>
:root{
  --page:#f6f5f7;
  --white:#ffffff;
  --navy:#14264d;
  --ink:#2b2f3a;
  --muted:#8a8d96;
  --orange:#e0552a;
  --accent:#ff5a1f;
  --sand:#ebe8e1;
  --rule:#1f2a44;
}
*{box-sizing:border-box;margin:0;padding:0}
html,body{width:1200px;height:3945px;overflow:hidden}
body{background:var(--page);font-family:'Lato',sans-serif;color:var(--navy);position:relative}
.slide{position:absolute;left:199px;width:802px;height:451px;background:var(--white);box-shadow:8px 12px 22px rgba(20,38,77,.14);overflow:hidden}
.abs{position:absolute}
.brand{display:flex;align-items:center;gap:8px;font-weight:700;color:var(--orange)}
.brand .dot{width:24px;height:24px;border-radius:50%;border:2px solid var(--orange)}
.brand-lg{font-size:23px}
.title{font-weight:700;font-size:26px;color:var(--navy);white-space:nowrap}
.subtitle{font-size:13px;font-weight:400;color:var(--navy)}
.presenter{font-size:15px;font-weight:400;color:var(--ink)}
.presenter b{font-weight:700;color:var(--orange)}
.center{left:0;right:0;text-align:center}
.bar{position:absolute;height:3px;width:37px;background:var(--orange)}
.bar-c{left:382px;top:34px}
.head{top:46px;font-size:26px;font-weight:700}
.kicker{top:84px;font-size:9px;font-weight:400;color:var(--muted)}
.footer{position:absolute;left:34px;right:32px;top:408px;border-top:1px solid var(--orange);height:30px;font-size:8px;font-weight:400;color:var(--ink)}
.footer .brand{position:absolute;left:0;top:8px;font-size:11px;gap:5px}
.footer .brand .dot{width:13px;height:13px;border-width:1.5px}
.footer .site{position:absolute;left:0;right:0;top:13px;text-align:center}
.footer .pg{position:absolute;right:8px;top:13px}
.footer .pg span{color:var(--orange);margin:0 10px}
.toc-item{position:absolute;width:245px;height:24px;border-bottom:2px solid var(--rule);display:flex;justify-content:space-between;align-items:flex-end;padding:0 2px 6px;font-size:10px;font-weight:700;color:var(--navy)}
.toc-item.active{border-bottom-color:var(--orange)}
.quote-box{left:99px;top:129px;width:603px;height:208px;background:var(--sand);box-shadow:5px 6px 12px rgba(0,0,0,.12);display:flex;align-items:center;justify-content:center;text-align:center;font-size:16px;font-weight:400;line-height:33px;color:var(--ink)}
.stat{position:absolute;width:158px;height:99px;background:var(--sand);box-shadow:4px 5px 10px rgba(0,0,0,.12);text-align:center;color:var(--navy)}
.stat .num{margin-top:20px;font-size:21px;font-weight:400}
.stat .dash{width:10px;height:2px;background:var(--orange);margin:4px auto 5px}
.stat .lbl{font-size:9px;font-weight:400;color:var(--ink)}
.stat.hot{background:var(--accent);color:var(--white)}
.stat.hot .lbl{color:var(--white)}
.stat.hot .dash{background:var(--white)}
.para{font-size:9px;font-weight:400;line-height:18px;color:var(--ink);text-align:center}
.photo{background:linear-gradient(180deg,#0a1a0c 0%,#124a18 40%,#1b1b22 75%,#0c0c10 100%)}
.mini-row{left:398px;top:239px;display:flex;align-items:center;box-shadow:4px 5px 10px rgba(0,0,0,.1)}
.mini{width:85px;height:78px;background:var(--white);text-align:center;color:var(--navy)}
.mini .num{margin-top:22px;font-size:18px;font-weight:400}
.mini .lbl{font-size:8px;font-weight:400;color:var(--muted);margin-top:4px}
.mini.hot{width:98px;height:86px;background:var(--accent);color:var(--white)}
.mini.hot .num{margin-top:26px}
.mini.hot .lbl{color:var(--white)}
.banner{left:43px;top:0;width:716px;height:260px;border-radius:0 0 44px 44px;background:linear-gradient(180deg,#26396a 0%,#1c2f5c 60%,#223663 100%)}
.card{position:absolute;top:278px;width:206px;height:128px;background:var(--sand);box-shadow:4px 5px 10px rgba(0,0,0,.12);text-align:center;color:var(--navy)}
.card .ico{width:24px;height:24px;border-radius:50%;background:#e87a5e;margin:16px auto 0;display:flex;align-items:center;justify-content:center}
.card h3{font-size:9px;font-weight:700;margin-top:11px}
.card .dash{width:10px;height:2px;background:var(--orange);margin:5px auto 6px}
.card p{font-size:8px;font-weight:400;line-height:18px;color:var(--ink);padding:0 20px}
.card.hot{background:var(--accent);color:var(--white)}
.card.hot p{color:var(--white)}
.card.hot .ico{background:rgba(255,255,255,.35)}
.card.hot .dash{background:var(--white)}
</style>
</head>
<body>

<section class="slide" style="top:145px">
  <div class="abs brand brand-lg" style="left:46px;top:100px"><span class="dot"></span>Velmarq</div>
  <div class="abs title" style="left:51px;top:188px">Presentation Title Here</div>
  <div class="abs subtitle" style="left:51px;top:232px">Subtitle Goes Here</div>
  <div class="abs presenter" style="left:51px;top:302px">Mr. Daan <b>Verhoef</b></div>
  <div class="abs" role="img" aria-label="Illustration of a lightbulb shaped as a head with a connected brain network" style="left:470px;top:80px;width:230px;height:275px;border-radius:48% 48% 30% 30%;background:radial-gradient(circle at 50% 35%,#f3b9a4 0%,#ec8a68 55%,#e0552a 100%)"></div>
</section>

<section class="slide" style="top:680px">
  <div class="abs brand brand-lg" style="left:0;right:0;justify-content:center;top:108px"><span class="dot"></span>Velmarq</div>
  <div class="abs title center" style="top:196px">Presentation Title Here</div>
  <div class="abs subtitle center" style="top:240px">Subtitle Goes Here</div>
  <div class="abs presenter center" style="top:311px">Mr. Daan <b>Verhoef</b></div>
  <div class="abs" style="left:38px;top:406px;font-size:10px;color:var(--ink)">May 2024</div>
  <div class="abs" style="right:38px;top:406px;font-size:10px;color:var(--ink)">www.website.com</div>
</section>

<section class="slide" style="top:1214px">
  <div class="bar bar-c"></div>
  <h2 class="abs head center">Presentation List</h2>
  <div class="abs kicker center">Here Our Subtitle</div>
  <div class="toc-item" style="left:104px;top:144px"><span>COVER SLIDES</span><span>01</span></div>
  <div class="toc-item active" style="left:104px;top:202px"><span>PRESENTATION LIST</span><span>03</span></div>
  <div class="toc-item" style="left:104px;top:260px"><span>ABOUT US</span><span>04</span></div>
  <div class="toc-item" style="left:104px;top:318px"><span>OUR MISSIONS &amp; VISION</span><span>06</span></div>
  <div class="toc-item" style="left:451px;top:144px"><span>INFOGRAPH ONE</span><span>07</span></div>
  <div class="toc-item" style="left:451px;top:202px"><span>INFOGRAPH TWO</span><span>08</span></div>
  <div class="toc-item" style="left:451px;top:260px"><span>INFOGRAPH THREE</span><span>09</span></div>
  <div class="toc-item" style="left:451px;top:318px"><span>CLOSING SLIDES</span><span>10</span></div>
  <footer class="footer"><div class="brand"><span class="dot"></span>Velmarq</div><div class="site">www.website.com</div><div class="pg">Page<span>|</span>3</div></footer>
</section>

<section class="slide" style="top:1749px">
  <div class="bar bar-c"></div>
  <h2 class="abs head center">Our Vision</h2>
  <div class="abs kicker center">Here Our Subtitle</div>
  <div class="abs quote-box"><p>Lorem ipsum dolor sit amet, consectetuer adipiscing elit.<br>Maecenas porttitor congue massa. Fusce posuere, magna<br>sed pulvinar ultricies, purus lectus malesuada libero.</p></div>
  <footer class="footer"><div class="brand"><span class="dot"></span>Velmarq</div><div class="site">www.website.com</div><div class="pg">Page<span>|</span>4</div></footer>
</section>

<section class="slide" style="top:2284px">
  <div class="bar bar-c"></div>
  <h2 class="abs head center">About Us</h2>
  <p class="abs para" style="left:96px;width:610px;top:133px"><b>Lorem ipsum</b> dolor sit amet, consectetuer adipiscing elit. Maecenas porttitor congue massa. Fusce posuere, magna sed pulvinar ultricies, purus lectus malesuada libero, sit amet commodo magna eros quis urna. Nunc viverra imperdiet enim. Fusce est. Vivamus a tellus. Pellentesque habitant morbi tristique senectus et netus et malesuada.</p>
  <div class="stat" style="left:54px;top:242px"><div class="num">25+</div><div class="dash"></div><div class="lbl">Years Solutions Expertise</div></div>
  <div class="stat hot" style="left:233px;top:242px"><div class="num">8K</div><div class="dash"></div><div class="lbl">Satisfy Costumer</div></div>
  <div class="stat" style="left:413px;top:242px"><div class="num">7500+</div><div class="dash"></div><div class="lbl">Working Hour</div></div>
  <div class="stat" style="left:592px;top:242px"><div class="num">138</div><div class="dash"></div><div class="lbl">Partner Business</div></div>
  <footer class="footer"><div class="brand"><span class="dot"></span>Velmarq</div><div class="site">www.website.com</div><div class="pg">Page<span>|</span>5</div></footer>
</section>

<section class="slide" style="top:2819px">
  <div class="abs photo" role="img" aria-label="Photo of a trading screen with green market data and app icons" style="left:83px;top:112px;width:272px;height:211px;box-shadow:4px 6px 12px rgba(0,0,0,.18)"></div>
  <div class="bar" style="left:398px;top:112px"></div>
  <h2 class="abs" style="left:398px;top:128px;font-size:25px;font-weight:700;white-space:nowrap">Business Support Legacy</h2>
  <p class="abs" style="left:398px;top:183px;width:335px;font-size:8.5px;font-weight:400;line-height:16px;color:var(--ink)">Lorem ipsum dolor sit amet, consectetuer adipiscing elit. Maecenas porttitor congue massa. Fusce posuere, magna sed pulvinar ultricies.</p>
  <div class="abs mini-row">
    <div class="mini"><div class="num">12+</div><div class="lbl">Partnership</div></div>
    <div class="mini hot"><div class="num">870+</div><div class="lbl">Satisfy Costumer</div></div>
    <div class="mini"><div class="num">200+</div><div class="lbl">Employee</div></div>
  </div>
  <footer class="footer"><div class="brand"><span class="dot"></span>Velmarq</div><div class="site">www.website.com</div><div class="pg">Page<span>|</span>6</div></footer>
</section>

<section class="slide" style="top:3353px">
  <div class="abs banner" role="img" aria-label="Photo of an open-plan office with people at desks, tinted navy"></div>
  <div class="bar" style="left:382px;top:77px"></div>
  <h2 class="abs center" style="top:97px;font-size:27px;font-weight:400;color:var(--white)">We’re Professional</h2>
  <div class="abs center" style="top:136px;font-size:12px;font-weight:400;color:var(--white)">Lorem ipsum dolor sit amet, consectetuer adipiscing elit.</div>
  <div class="card" style="left:34px"><div class="ico"><svg width="12" height="12" viewBox="0 0 12 12"><path d="M6 2 L10 10 H2 Z" fill="#fff"/></svg></div><h3>Professional One</h3><div class="dash"></div><p>Lorem ipsum dolor sit amet, consectetuer adipiscing elit.</p></div>
  <div class="card hot" style="left:298px"><div class="ico"><svg width="12" height="12" viewBox="0 0 12 12"><circle cx="6" cy="5" r="3" fill="#fff"/><rect x="4.5" y="8.5" width="3" height="2" fill="#fff"/></svg></div><h3>Professional Two</h3><div class="dash"></div><p>Lorem ipsum dolor sit amet, consectetuer adipiscing elit.</p></div>
  <div class="card" style="left:563px"><div class="ico"><svg width="12" height="12" viewBox="0 0 12 12"><circle cx="6" cy="4.5" r="2.3" fill="#fff"/><path d="M2 11 Q6 5.5 10 11 Z" fill="#fff"/></svg></div><h3>Professional Three</h3><div class="dash"></div><p>Lorem ipsum dolor sit amet, consectetuer adipiscing elit.</p></div>
  <footer class="footer"><div class="brand"><span class="dot"></span>Velmarq</div><div class="site">www.website.com</div><div class="pg">Page<span>|</span>7</div></footer>
</section>

</body>
</html>
```